Naturopath Practitioner Card Design

I am a naturopath needing a design for a business card mainly to show that I am a naturopath and have some contact details to give to prospective clients. I am open minded about the design and what is on the second side of the card whether it just be some artwork or space for details, appointment times etc. Naturopathy is the practice of natural medicine that uses a holistic approach and incorporates herbal and nutritional medicine.

Industry/Entity Type

Business

Contact Information for Business Card

Tom Welby NaturopathBHSc (Naturopathy) Member PHRA 0492 815 306 tom.welby@mailbright.com www.tomwelbynaturopathy.com.au

Requirements
Nice to have
• Would prefer some kind of original pattern/art work/logo rather than an image, not fussed if its very simple/basic
• I am open to any colour but think I would prefer a more earthy sandy clay etc type style than the greens that are commonly associated with naturopathy.
Should not have
• Don't really want to have generic stock images on it

```html
<!DOCTYPE html>
<html lang="en">
<head>
<meta charset="utf-8">
<title>Tom Welby Naturopath – Business Card</title>
<link rel="stylesheet" href="https://fonts.googleapis.com/css2?family=Open+Sans:wght@400;600;700&display=swap">
<style>
  :root {
    --page-bg: #ece8e2;
    --card-bg: #ffffff;
    --leaf-green: #2f9e1f;
    --leaf-light: #b9e08a;
    --leaf-mid: #6cc23a;
    --leaf-deep: #2e7d12;
    --ink: #1f1f1f;
    --ink-soft: #333333;
    --dots: #444444;
  }
  * { box-sizing: border-box; margin: 0; padding: 0; }
  html, body {
    width: 1200px; height: 900px; overflow: hidden;
    background: var(--page-bg);
    font-family: "Open Sans", Arial, sans-serif;
  }
  .canvas {
    width: 1200px; height: 900px;
    display: flex; flex-direction: column; align-items: center; justify-content: center;
    gap: 40px;
  }
  .card {
    position: relative;
    width: 700px; height: 400px;
    background: var(--card-bg);
    overflow: hidden;
    box-shadow: 0 6px 18px rgba(0,0,0,0.12);
  }

  /* ---------- Appointment side ---------- */
  .appointment { padding: 42px 48px; }
  .appointment__title {
    color: var(--leaf-green);
    font-weight: 700; font-size: 25px;
  }
  .appointment__line {
    display: block; margin: 4px 0 0 0;
    border-bottom: 2px dotted var(--dots);
    width: 94%; height: 4px;
  }
  .appointment__row {
    display: flex; align-items: flex-end; gap: 10px;
    margin-top: 30px;
    color: var(--ink); font-weight: 700; font-size: 19px;
  }
  .appointment__fill {
    flex: 0 0 auto; border-bottom: 2px dotted var(--dots); height: 18px;
  }
  .appointment__fill--name { width: 430px; }
  .appointment__fill--date { width: 160px; }
  .appointment__fill--time { width: 130px; }
  .appointment__ampm { font-weight: 400; font-size: 16px; }
  .appointment__notice {
    margin-top: 30px;
    color: var(--leaf-green); font-weight: 600; font-size: 17px;
  }
  .appointment__foliage {
    position: absolute; left: 0; right: 0; bottom: 0; height: 120px;
    background: linear-gradient(8deg, var(--leaf-deep) 0%, var(--leaf-mid) 45%, rgba(108,194,58,0.35) 75%, rgba(255,255,255,0) 100%);
    clip-path: polygon(0 70%, 20% 62%, 40% 55%, 60% 35%, 80% 15%, 100% 0, 100% 100%, 0 100%);
  }

  /* ---------- Contact side ---------- */
  .contact__photo {
    position: absolute; left: 0; top: 0; bottom: 0; width: 460px;
    background:
      radial-gradient(ellipse at 35% 60%, rgba(76,170,40,0.9) 0%, rgba(108,194,58,0.7) 35%, rgba(185,224,138,0.4) 65%, rgba(255,255,255,0) 90%),
      linear-gradient(90deg, var(--leaf-light) 0%, rgba(200,235,160,0.6) 55%, rgba(255,255,255,0) 100%);
  }
  .contact__details {
    position: absolute; left: 390px; right: 24px; top: 80px;
    color: var(--ink-soft);
  }
  .contact__name {
    color: var(--leaf-green); font-weight: 700; font-size: 22px;
  }
  .contact__role, .contact__credentials { font-size: 14px; margin-top: 4px; margin-left: 14px; }
  .contact__list { list-style: none; margin: 30px 0 0 40px; font-size: 15px; }
  .contact__item { display: flex; align-items: center; gap: 8px; margin-bottom: 6px; white-space: nowrap; }
  .contact__icon { width: 13px; height: 13px; fill: var(--leaf-green); flex: 0 0 auto; }
</style>
</head>
<body>
<main class="canvas">

  <section class="card appointment" aria-label="Appointment card">
    <h2 class="appointment__title">Your Next Appointment on</h2>
    <span class="appointment__line"></span>
    <div class="appointment__row">Name : <span class="appointment__fill appointment__fill--name"></span></div>
    <div class="appointment__row">
      Date : <span class="appointment__fill appointment__fill--date"></span>
      &nbsp;Time : <span class="appointment__fill appointment__fill--time"></span>
      <span class="appointment__ampm">AM / PM</span>
    </div>
    <p class="appointment__notice">If unable to keep appointment, kindly give 24hrs notice.</p>
    <div class="appointment__foliage" role="img" aria-label="Border of fresh green leaves along the bottom edge"></div>
  </section>

  <section class="card contact" aria-label="Contact card">
    <div class="contact__photo" role="img" aria-label="Close-up of green leaves with water droplets on a soft bokeh background"></div>
    <div class="contact__details">
      <h1 class="contact__name">Tom Welby</h1>
      <p class="contact__role">Naturopath</p>
      <p class="contact__credentials">BHSc (Naturopathy) Member PHRA</p>
      <ul class="contact__list">
        <li class="contact__item">
          <svg class="contact__icon" viewBox="0 0 24 24" aria-hidden="true"><path d="M6.6 10.8a15 15 0 0 0 6.6 6.6l2.2-2.2a1 1 0 0 1 1-.25 11.4 11.4 0 0 0 3.6.57 1 1 0 0 1 1 1V20a1 1 0 0 1-1 1A17 17 0 0 1 3 4a1 1 0 0 1 1-1h3.5a1 1 0 0 1 1 1c0 1.25.2 2.45.57 3.6a1 1 0 0 1-.25 1z"/></svg>
          0492 815 306
        </li>
        <li class="contact__item">
          <svg class="contact__icon" viewBox="0 0 24 24" aria-hidden="true"><path d="M2 5h20v14H2z M2 5l10 8 10-8" stroke="#fff" stroke-width="1.5"/></svg>
          tom.welby@mailbright.com
        </li>
      </ul>
    </div>
  </section>

</main>
</body>
</html>
```